" Pessoal, vamos lá! Estivemos trabalhando bastante e definindo o formato da nossa empresa e agora chegou a hora de passarmos para o nosso web site. Vamos lá: O " ÍNDICE" deverá conter: Nossos Serviços, Sua obra viva Protegida, Tudo Melhor para Você, Peça um orçamento. 1- Ao clicar na aba Nossos Serviços. Será direcionado para Reforma & Construção; e Assessoria. Nesse campo terá as seguintes informações: Reforma & Construção * Projeto Guia de Reforma Fornecemos a planta com alterações e novas medidas. * Orçamento Enviamos nossa proposta de orçamento totalmente grátis. * Acompanhamento de Engenheiro Civil e Arquiteto* Equipe de profissionais capacitados. * Cotação de melhores preços de materiais; Auxiliamos na busca de melhores preços e condições de pagamento para a sua obra viva ou obra. * Seleção de parceiros para execução; Selecionamos profissionais capacitados para a execução da sua obra viva ou obra. Assessoria * Acompanhamos o projeto em execução Acompanhamento das atividades associadas ao planejamento, organização, direção e controle necessários para garantir o sucesso da sua obra viva ou obra. * Programação da Obra Compreendendo o detalhamento dos serviços e as providências preliminares, a programação dos materiais, mão de obra e equipamentos. * Relatórios de Andamento da obra Adequação do projeto e da construção às necessidades do cliente no que se refere à qualidade, prazo e custo. 2- Na aba " sua obra viva protegida" ao clicar será direcionado para o campo com as seguintes informações: * Substituição de materiais danificados Qualquer material danificado por nossos profissionais ou fornecedores são repostos na mesma qualidade e quantidade, sem custos para o cliente. * Correção dos serviços mal executados* Mesmo buscando fornecer o resultado que você espera e sempre trabalhando com profissionais capacitados, erros podem acontecer. Diante disso, asseguramos a conclusão da sua obra com qualidade. * Troca de fornecedor Selecionamos os melhores profissionais do mercado. Mesmo assim, se você não gostar, é livre para nos solicitar a troca. 3- Já na aba " Tudo melhor para você" teremos as seguintes informações: * Orçamento gratuito * Gestão de pagamento * Prazo e rapidez * Saiba tudo que está acontecendo na sua obra viva * Garantia de Satisfação * Consultoria Técnica * Cronograma de gerenciamento * Otimização de custos * Equipe preparada 4- Seja um Novo Parceiro Ao clicar nessa frase aparecerá em uma nova janela duas opçoes: EMPRESA e PROFISSIONAL. Clicando em EMPRESA ficará a disposição para preenchimento os seguintes campos: Nome da Empresa, Nome do Responsável, Cidade, email, contato, área de especialidade ( nesse campo existirá opções para preenchimento) e campo para apresentação da empresa. Se clicar em PROFISSIONAL terá a disposição os seguintes itens: Nome, Telefone, cidade, email e área de especialidade (também várias opções )e um campo para digitação chamado de ESCREVA AQUI SUA MENSAGEM. 5- ORÇAMENTO Após o clique no ORÇAMENTO, o cliente terá à disposição 3 opções para um novo clique: REFORMA, CONSTRUÇÃO, ASSESSORIA (se possível, adicionar imagens aos nomes) • Após o clique em REFORMA abrirá um formulário com opções: Campo com opções de escolha de Casa, Apartamento ou loja comercial; Escolha do Cômodo (terá opções nesse campo) e nova janela referente a esta escolha para a digitação do tipo de serviço a ser executado nesse campo. Caso existam mais cômodos, existirá a opção de adicionar; opção de upload de arquivo; e campo para escrever alguma mensagem ou observação. • Clicando em CONSTRUÇÃO – O que pretende construir?; descreva detalhadamente o que pretende construir; opção de upload de arquivo; e campo para escrever alguma mensagem ou observação. • ASSESSORIA – Ajudamos você na gestão da sua obra viva. Como podemos ajudar? (aparecerá as opções de Cotação de preços; Busca de profissionais; Conferência e acompanhamento de serviços executados); descreva detalhadamente que tipo de ajuda você precisa em sua obra. 5.1 Ao final de todas as opções aparecerá campo para preenchimento dos dados do cliente: Seu nome; email; CEP; Rua; Numero/complemento; Bairro; Cidade; Estado; Telefone; e campo para clique em Aceito e concordo com os Termos de Uso e a Política de Privacidade. Confirmar envio da solicitação Para auxiliá-los vejam o site http://www.lajetorvix.com.br/orcamento.html 6- Vale lembrar que em cada aba terá que ser visualizado a opção de PEÇA UM ORÇAMENTO, FAÇA SUA OBRA VIVA, SUA OBRA VIVA AGORA.... FIQUEM A VONTADE com os dizeres. - Ao Final, na parte de contatos, endereço, rede social.... etc. Gostaríamos de deixar o espaço SEJA UM PARCEIRO. Queremos que ao clicar nessa item a empresa preencha um questionário. 7- Vale lembrar que ao clicar no item Peça orçamento o cliente será direcionado para um campo de preenchimento de dados. OBS IMPORTANTE: - Façam o uso de imagens modernas e suaves.. Queremos ser diferentes e inovadores e precisamos muito da criatividade de vocês. - Segue anexo um modelo de imagem que gostamos Segue anexo do escopo do nosso portfólio que será a cópia do nosso site. Aproveitem. "

```html
<!DOCTYPE html>
<html lang="pt-BR">
<head>
<meta charset="utf-8">
<title>Obra Viva — Reforma e construção</title>
<link href="https://fonts.googleapis.com/css2?family=Open+Sans:wght@400;600;700&family=Montserrat:wght@600;700&display=swap" rel="stylesheet">
<style>
  :root{
    --navy:#1d3b63;
    --navy-dark:#132a48;
    --ink:#2d3440;
    --muted:#7c8591;
    --line:#d9dde3;
    --icon-bg:#e4e7eb;
    --white:#ffffff;
    --page:#f4f5f7;
  }
  *{box-sizing:border-box;margin:0;padding:0}
  html,body{width:1200px;height:1200px;overflow:hidden}
  body{background:var(--white);font-family:"Open Sans",Arial,sans-serif;color:var(--ink)}

  .site-header{position:absolute;top:0;left:0;width:1200px;height:72px;display:flex;align-items:center;padding:0 48px;background:rgba(19,42,72,.55);z-index:2}
  .brand{color:var(--white);font-size:24px;font-weight:600;white-space:nowrap}
  .main-nav{margin-left:auto;display:flex;align-items:center;gap:30px;font-size:12px;font-weight:700;letter-spacing:.04em;color:var(--white);text-transform:uppercase;white-space:nowrap}
  .social-dot{width:14px;height:14px;background:var(--white);border-radius:2px}
  .nav-cta{background:var(--navy);padding:9px 16px;border-radius:2px}

  .hero{position:relative;height:520px;overflow:hidden}
  .hero-photo{position:absolute;inset:0;background:linear-gradient(120deg,#5d6f86 0%,#8a9bb0 35%,#3e5675 60%,#6e7f93 100%)}
  .hero-shade{position:absolute;inset:0;background:rgba(20,32,50,.45)}
  .hero-title{position:absolute;top:210px;width:100%;text-align:center;color:var(--white);font-family:"Montserrat","Open Sans",sans-serif;text-transform:uppercase}
  .hero-title h1{font-size:62px;font-weight:700;letter-spacing:.12em;white-space:nowrap}
  .hero-title p{margin-top:12px;font-size:34px;font-weight:600;letter-spacing:.1em;white-space:nowrap}

  .section-title{font-family:"Montserrat","Open Sans",sans-serif;font-weight:600;color:var(--navy);text-align:center;letter-spacing:.06em}

  .protected{height:300px;padding-top:36px;background:var(--white)}
  .protected .section-title{font-size:40px}
  .feature-row{display:flex;justify-content:center;gap:80px;margin-top:34px}
  .feature{width:300px;text-align:center}
  .feature h3{font-size:14px;font-weight:700;text-transform:uppercase;line-height:1.35;color:var(--ink)}
  .feature p{margin-top:10px;font-size:12px;line-height:1.6;color:var(--muted)}

  .advisory{height:308px;padding-top:22px;background:var(--page);border-top:1px solid var(--line)}
  .advisory .section-title{font-size:28px;letter-spacing:.14em}
  .advisory .rule{width:220px;height:2px;background:var(--navy);margin:8px auto 0}
  .service-row{display:flex;justify-content:center;gap:60px;margin-top:22px}
  .service{width:230px;text-align:center}
  .service h3{font-size:11px;font-weight:700;text-transform:uppercase;line-height:1.35}
  .service p{margin-top:6px;font-size:10px;line-height:1.5;color:var(--muted);height:30px;overflow:hidden}
  .icon-circle{width:76px;height:76px;border-radius:50%;background:var(--icon-bg);margin:10px auto 0;display:flex;align-items:center;justify-content:center}
  .icon-circle.is-active{background:var(--navy)}
  .cta{display:block;width:max-content;margin:22px auto 0;background:var(--navy);color:var(--white);font-size:13px;font-weight:700;text-transform:uppercase;padding:11px 22px;border-radius:2px;letter-spacing:.03em}

  .interior-strip{height:80px;background:linear-gradient(90deg,#b7b1a7,#d6d2cb 40%,#a9a59d 70%,#c9c4bb)}
</style>
</head>
<body>
  <header class="site-header">
    <div class="brand">obra viva</div>
    <nav class="main-nav">
      <span>Nossos serviços</span>
      <span>Sua obra viva protegida</span>
      <span>Tudo melhor para você</span>
      <span class="social-dot"></span>
      <span class="nav-cta">Orçamento</span>
    </nav>
  </header>

  <section class="hero">
    <div class="hero-photo" role="img" aria-label="Fotografia de profissional de reforma trabalhando em escada dentro de um ambiente em obra"></div>
    <div class="hero-shade"></div>
    <div class="hero-title">
      <h1>Sua obra viva</h1>
      <p>Com quem entende do assunto !</p>
    </div>
  </section>

  <section class="protected">
    <h2 class="section-title">Sua obra viva protegida</h2>
    <div class="feature-row">
      <div class="feature">
        <h3>Substituição de<br>materiais danificados</h3>
        <p>Qualquer material danificado por nossos profissionais ou fornecedores é reposto na mesma qualidade e quantidade, sem custos.</p>
      </div>
      <div class="feature">
        <h3>Correção dos serviços<br>mal executados</h3>
        <p>Erros podem acontecer. Diante disso, asseguramos a conclusão da sua obra com qualidade.</p>
      </div>
      <div class="feature">
        <h3>Troca de<br>fornecedor</h3>
        <p>Selecionamos os melhores profissionais do mercado. Se você não gostar, é livre para solicitar a troca.</p>
      </div>
    </div>
  </section>

  <section class="advisory">
    <h2 class="section-title">Assessoria</h2>
    <div class="rule"></div>
    <div class="service-row">
      <div class="service">
        <h3>Acompanhamos<br>o projeto em execução</h3>
        <p>Planejamento, organização, direção e controle para o sucesso da sua obra.</p>
        <div class="icon-circle">
          <svg width="38" height="38" viewBox="0 0 38 38" fill="none" stroke="#4a5563" stroke-width="2.4" stroke-linecap="round"><line x1="8" y1="8" x2="30" y2="30"/><line x1="30" y1="8" x2="8" y2="30"/><line x1="26" y1="5" x2="33" y2="12"/></svg>
        </div>
      </div>
      <div class="service">
        <h3>Programação<br>da obra</h3>
        <p>Detalhamento dos serviços, materiais, mão de obra e equipamentos.</p>
        <div class="icon-circle is-active">
          <svg width="40" height="40" viewBox="0 0 40 40" fill="none" stroke="#fff" stroke-width="2.4" stroke-linecap="round"><path d="M31 13a13 13 0 1 0 2 9"/><polyline points="32,6 32,13 25,13"/><polyline points="20,12 20,21 26,24"/></svg>
        </div>
      </div>
      <div class="service">
        <h3>Relatórios de<br>andamento da obra</h3>
        <p>Adequação do projeto quanto à qualidade, prazo e custo da obra.</p>
        <div class="icon-circle">
          <svg width="34" height="38" viewBox="0 0 34 38" fill="none" stroke="#4a5563" stroke-width="2.2"><rect x="5" y="3" width="24" height="32" rx="2"/><rect x="10" y="10" width="14" height="9"/><line x1="10" y1="25" x2="24" y2="25"/><line x1="10" y1="30" x2="20" y2="30"/></svg>
        </div>
      </div>
    </div>
    <span class="cta">Comece agora sua obra viva</span>
  </section>

  <div class="interior-strip" role="img" aria-label="Fotografia de ambiente interno reformado"></div>
</body>
</html>
```